Lantern Harbor of Alabama

We are a disaster relief nonprofit organization that provides relief to families children and pets when a disaster strikes multifamily. We need a easy and powerful piece that tells what we do and draws folks into finding out more. So a piece that could be used at tradeshows or speaking engagements
Updates

Be sure to include our social and other contact info. Added Monday, October 16, 2017

Target Market(s)

Potential Donors & Volunteers

Industry/Entity Type

Non-Profit

Font styles to use
Serif

Colors

Designer to choose colors to be used in the design.

Requirements
Must have
• Our logo and trigger photos I am going to rely on your expertise to create something compelling that is simple and powerful
Nice to have
• Moving pull on the heart strings

```html
<!DOCTYPE html>
<html lang="en">
<head>
<meta charset="utf-8">
<title>Lantern Harbor of Alabama – Disaster Relief Kit</title>
<link rel="stylesheet" href="https://fonts.googleapis.com/css2?family=Cormorant+Garamond:wght@300;500&family=Rajdhani:wght@400;500;600;700&display=swap">
<style>
  :root{
    --paper:#f6f6f4;
    --ink:#2b2b2b;
    --grey:#6d6d6d;
    --gold:#f5bf3c;
    --coral:#ee7f5c;
    --rust:#d8603f;
    --teal:#1c5f68;
    --teal-ring:#cfe0cf;
    --blue:#2a6e9e;
    --sky:#39a7d6;
    --lime:#8dc63f;
    --red:#e5412f;
  }
  *{margin:0;padding:0;box-sizing:border-box}
  html,body{width:950px;height:1200px;overflow:hidden;background:var(--paper)}
  .flyer{position:relative;width:950px;height:1200px;background:var(--paper);font-family:"Rajdhani",sans-serif;color:var(--ink)}
  .art{position:absolute;inset:0}
  .brand{position:absolute;left:40px;top:46px;font-family:"Cormorant Garamond",serif;font-weight:300;color:var(--grey);line-height:.95}
  .brand .line1{font-size:92px;display:block}
  .brand .line2{font-size:92px;display:block;padding-left:30px}
  .brand .line3{font-size:32px;display:block;padding-left:150px;margin-top:8px}
  .quote{position:absolute;left:40px;top:320px;width:400px;font-family:"Cormorant Garamond",serif;font-weight:500;font-size:29px;line-height:1.2;text-transform:uppercase;white-space:nowrap}
  .quote .mark{color:var(--gold);font-size:60px;line-height:0;vertical-align:-22px;font-weight:500}
  .quote .l1,.quote .l2{display:block}
  .quote .l2{padding-left:58px}
  .cite{position:absolute;left:40px;width:392px;top:414px;text-align:right;font-family:"Cormorant Garamond",serif;font-size:22px;font-weight:500;color:var(--rust)}
  .mission{position:absolute;left:40px;top:452px;width:486px;font-size:22.5px;font-weight:400;line-height:1.24;text-align:justify}
  .kit-title{position:absolute;left:40px;top:551px;width:546px;height:42px;background:var(--coral);border-radius:6px;color:#fff;font-weight:700;font-size:30px;letter-spacing:.5px;line-height:42px;padding-left:12px}
  .kit-list{position:absolute;left:42px;top:604px;width:520px;list-style:none}
  .kit-list li{position:relative;padding-left:40px;font-size:26px;font-weight:600;line-height:35.5px}
  .kit-list li::before{content:"";position:absolute;left:0;top:9px;width:22px;height:22px;border-radius:50%;background:var(--gold)}
  .kit-list li::after{content:"";position:absolute;left:6px;top:16px;width:7px;height:7px;border-top:2.5px solid var(--rust);border-right:2.5px solid var(--rust);transform:rotate(45deg)}
  .about{position:absolute;left:598px;top:612px;width:340px;text-align:center;color:#fff;font-size:23px;font-weight:500;line-height:1.2;white-space:nowrap}
  .about strong{color:var(--gold);font-weight:700;display:block;text-transform:uppercase}
  .partners-label{position:absolute;left:598px;top:946px;font-size:17.5px;font-weight:600}
  .social{position:absolute;right:0;height:37px;color:#fff;font-weight:600;font-size:25px;line-height:37px;display:flex;align-items:center;gap:10px}
  .social .dot{width:22px;height:22px;border-radius:50%;background:#fff;flex:none}
  .social.fb{top:1084px;width:268px;background:var(--lime);padding-left:16px;clip-path:polygon(14px 0,100% 0,100% 100%,0 100%)}
  .social.web{top:1122px;width:440px;background:var(--blue);padding-left:24px;clip-path:polygon(14px 0,100% 0,100% 100%,0 100%)}
</style>
</head>
<body>
<main class="flyer">
  <svg class="art" width="950" height="1200" viewBox="0 0 950 1200">
    <circle cx="510" cy="50" r="38" fill="#f1a88e"/>
    <circle cx="775" cy="22" r="13" fill="#ee9a80"/>
    <line x1="857" y1="90" x2="857" y2="215" stroke="#a7d6dd" stroke-width="4"/>
    <circle cx="857" cy="90" r="18" fill="#a7d6dd"/>
    <circle cx="872" cy="160" r="19" fill="var(--gold)" opacity=".8"/>
    <circle cx="822" cy="180" r="28" fill="#f2e05a" opacity=".75"/>
    <circle cx="488" cy="255" r="11" fill="#c9a227"/>
    <line x1="718" y1="420" x2="718" y2="470" stroke="var(--lime)" stroke-width="4"/>
    <circle cx="718" cy="472" r="9" fill="var(--lime)"/>
    <circle cx="670" cy="408" r="36" fill="var(--sky)"/>
    <circle cx="812" cy="398" r="54" fill="#f5d96b" opacity=".85"/>
    <circle cx="770" cy="390" r="12" fill="var(--red)"/>
    <circle cx="880" cy="428" r="17" fill="#f2c6c0"/>
    <g role="img" aria-label="Photo of a smiling mother and son">
      <circle cx="655" cy="139" r="170" fill="#2d80b8"/>
    </g>
    <g role="img" aria-label="Photo of children holding donated teddy bears">
      <circle cx="547" cy="350" r="85" fill="#8a9a2e"/>
    </g>
    <g role="img" aria-label="Photo of a young child hugging a teddy bear">
      <circle cx="704" cy="361" r="66" fill="#c99a2a"/>
    </g>
    <g role="img" aria-label="Photo of a boy unpacking a relief kit">
      <circle cx="847" cy="294" r="100" fill="#c57a55"/>
    </g>
    <circle cx="752" cy="722" r="212" fill="var(--teal-ring)"/>
    <circle cx="752" cy="722" r="198" fill="var(--teal)"/>
    <rect x="604" y="992" width="100" height="26" rx="3" fill="#9aa3ad"/>
    <rect x="718" y="988" width="84" height="30" rx="3" fill="#3b6fa8"/>
    <rect x="820" y="986" width="80" height="36" rx="3" fill="#d9534f"/>
    <rect x="600" y="1040" width="76" height="26" rx="3" fill="#b33a2f"/>
    <rect x="684" y="1034" width="84" height="34" rx="3" fill="#2f78b8"/>
    <rect x="780" y="1038" width="116" height="28" rx="3" fill="#7fae5a"/>
    <circle cx="44" cy="1066" r="7" fill="#e89a84"/>
    <line x1="343" y1="1030" x2="343" y2="1110" stroke="#f1a88e" stroke-width="4"/>
    <circle cx="343" cy="1030" r="17" fill="var(--coral)"/>
    <circle cx="302" cy="1030" r="13" fill="#a7d6dd"/>
    <line x1="405" y1="1045" x2="405" y2="1120" stroke="#f4d58d" stroke-width="4"/>
    <circle cx="405" cy="1045" r="15" fill="#f4d58d"/>
    <circle cx="377" cy="1088" r="13" fill="#f5d96b"/>
    <circle cx="55" cy="1150" r="55" fill="#b9d98a"/>
    <g role="img" aria-label="Photo of rescuers guiding a boat of flood evacuees">
      <circle cx="161" cy="1062" r="122" fill="#1d4f78"/>
    </g>
    <g role="img" aria-label="Photo of a firefighter carrying a rescued dog">
      <circle cx="329" cy="1124" r="88" fill="#b8622e"/>
    </g>
    <circle cx="250" cy="1192" r="8" fill="var(--red)"/>
    <circle cx="210" cy="1196" r="7" fill="var(--sky)"/>
  </svg>

  <h1 class="brand">
    <span class="line1">Lantern</span>
    <span class="line2">Harbor</span>
    <span class="line3">of Alabama</span>
  </h1>

  <blockquote class="quote">
    <span class="l1"><span class="mark">“</span> He who has hope,</span>
    <span class="l2">has everything.<span class="mark">”</span></span>
  </blockquote>
  <p class="cite">– Edwin Marlowe</p>

  <p class="mission">We support residents that have been displaced from their apartment homes due to fire or other disasters.</p>

  <h2 class="kit-title">DISASTER RELIEF KIT SUPPLY LIST</h2>
  <ul class="kit-list">
    <li>Twin Air Mattress (8.00 at ValueMart)</li>
    <li>Standard Pillows (2.37 at ValueMart)</li>
    <li>Air Pumps (13.00 ValueMart)</li>
    <li>Blankets/Throws (2.88 at ValueMart)</li>
    <li>Towels/Washcloths/Flat Sheets</li>
    <li>Flip Flops- Solid Colors-All sizes<br>(ValueMart $1)</li>
    <li>Penny Depot Items All $1</li>
    <li>Cases of Bottled Water</li>
  </ul>

  <p class="about"><strong>Lantern Harbor of<br>Alabama is a Birmingham,</strong>Alabama based 501c3<br>nonprofit organization<br>that provides disaster<br>relief to Residents<br>displaced from Apartment<br>Homes across the state of<br>Alabama.</p>

  <p class="partners-label">Proud members in collaboration with:</p>

  <div class="social fb"><span class="dot"></span>LanternHarbor</div>
  <div class="social web"><span class="dot"></span>Lanternharborofalabama.org</div>
</main>
</body>
</html>
```